Business card for a plastic surgeon

i need a business card for a plastic surgeon. I have two adresses. The card should communicate safety, simmetry, beauty and with soft colors.
What i want in the card:
- my logo: Letters "R"and "B" (picture uploaded)
- my name: Renato Bastiani
- my registration: CRM 507 219
- my adresses and phone numbers (2):
- Av Dr Teixeira Lopes, 2710, sala 305 - Vila Olímpia | São Paulo/ SP - Phone: 11 4172-5036
- Al. Itapeva, 47, 3 andar - Alphaville | Barueri/ SP - Phone: 11 6350-2481

- my social network: site, facebook and instagram

Target Market(s)

people (95% girls and women) that want cosmetic procedures and plastic surgery

Industry/Entity Type

Business

Contact Information for Business Card

The card should communicate safety, simmetry, beauty and with soft colors.
Beige, brown, gray, rosy are some options. Color is free

Font styles to use
Serif

Requirements
Must have
• - my logo: Letters "R"and "B" (picture uploaded)
• - my name: Renato Bastiani
• - my registration: CRM 507 219
• - my adresses and phone numbers (2):
• - Av Dr Teixeira Lopes, 2710, sala 305 - Vila Olímpia | São Paulo/ SP - Phone: 11 4172-5036
• - Al. Itapeva, 47, 3 andar - Alphaville | Barueri/ SP - Phone: 11 6350-2481
• - my social network: site, facebook and instagram
Should not have
• other images (only my logo)

```html
<!DOCTYPE html>
<html lang="pt-BR">
<head>
<meta charset="UTF-8">
<title>Dr. Renato Bastiani – Cartão de Visita</title>
<link rel="stylesheet" href="https://fonts.googleapis.com/css2?family=Cinzel:wght@400;600;700&family=Open+Sans:wght@400;600&display=swap">
<style>
  :root {
    --taupe: #a58c76;
    --white: #ffffff;
    --backdrop: #2d2d2f;
    --card-w: 620px;
    --card-h: 354px;
  }
  * { margin: 0; padding: 0; box-sizing: border-box; }
  html, body {
    width: 1200px;
    height: 880px;
    overflow: hidden;
    background: var(--backdrop);
  }
  .canvas {
    position: relative;
    width: 1200px;
    height: 880px;
  }
  .card {
    position: absolute;
    width: var(--card-w);
    height: var(--card-h);
    border-radius: 22px;
    overflow: hidden;
    box-shadow: 0 14px 34px rgba(0,0,0,0.45);
  }
  .card-front {
    left: 70px;
    top: 70px;
    background: var(--taupe);
  }
  .card-back {
    left: 510px;
    top: 456px;
    background: var(--white);
  }
  .card-shape {
    position: absolute;
    inset: 0;
  }

  /* brand lockup */
  .lockup {
    position: absolute;
    text-align: center;
    font-family: "Cinzel", serif;
  }
  .lockup-mark {
    display: block;
    margin: 0 auto 14px;
    border-radius: 50%;
  }
  .lockup-name {
    font-weight: 400;
    letter-spacing: 0.03em;
    white-space: nowrap;
  }
  .lockup-title {
    font-weight: 400;
    letter-spacing: 0.32em;
    white-space: nowrap;
  }
  .card-front .lockup {
    left: 0; right: 0;
    top: 100px;
    color: var(--white);
  }
  .card-front .lockup-mark {
    width: 44px; height: 44px;
    border: 2px solid var(--white);
  }
  .card-front .lockup-name { font-size: 27px; }
  .card-front .lockup-title { font-size: 13px; margin-top: 4px; }

  .card-back .lockup {
    left: 24px;
    width: 290px;
    top: 118px;
    color: var(--taupe);
  }
  .card-back .lockup-mark {
    width: 34px; height: 34px;
    border: 2px solid var(--taupe);
  }
  .card-back .lockup-name { font-size: 19px; }
  .card-back .lockup-title { font-size: 10px; margin-top: 3px; }

  /* contact details */
  .contact {
    position: absolute;
    left: 392px;
    top: 44px;
    width: 210px;
    color: var(--white);
    font-family: "Open Sans", sans-serif;
  }
  .contact-name {
    font-family: "Cinzel", serif;
    font-weight: 700;
    font-size: 19px;
    letter-spacing: 0.02em;
    white-space: nowrap;
  }
  .contact-reg {
    font-size: 12px;
    margin: 2px 0 0 2px;
  }
  .address {
    margin-top: 22px;
    padding-left: 22px;
    font-size: 12.5px;
    line-height: 1.42;
  }
  .address + .address { margin-top: 16px; }
  .phone {
    display: flex;
    align-items: center;
    gap: 6px;
  }
  .phone-icon {
    width: 14px;
    height: 12px;
    flex: none;
  }
</style>
</head>
<body>
<main class="canvas">

  <section class="card card-front" aria-label="Frente do cartão">
    <div class="lockup">
      <span class="lockup-mark"></span>
      <p class="lockup-name">Dr. Renato Bastiani</p>
      <p class="lockup-title">Cirurgião Plástico</p>
    </div>
  </section>

  <section class="card card-back" aria-label="Verso do cartão">
    <svg class="card-shape" viewBox="0 0 620 354" preserveAspectRatio="none" aria-hidden="true">
      <path d="M342,0 C300,110 400,230 340,354 L620,354 L620,0 Z" fill="var(--taupe)"/>
      <path d="M324,0 C282,110 382,230 322,354" fill="none" stroke="var(--taupe)" stroke-width="6"/>
    </svg>

    <div class="lockup">
      <span class="lockup-mark"></span>
      <p class="lockup-name">Dr. Renato Bastiani</p>
      <p class="lockup-title">Cirurgião Plástico</p>
    </div>

    <div class="contact">
      <p class="contact-name">Renato Bastiani</p>
      <p class="contact-reg">CRM 507 219</p>

      <div class="address">
        <p>Av Dr Teixeira Lopes,</p>
        <p>2710, sala 305</p>
        <p>Vila Olímpia | São Paulo/ SP</p>
        <p class="phone">
          <svg class="phone-icon" viewBox="0 0 14 12" aria-hidden="true">
            <rect x="0" y="0" width="14" height="12" rx="2" fill="var(--white)"/>
            <path d="M3,4 Q7,1 11,4 L10,5.5 L8.5,4.8 L8.5,4 Q7,3.4 5.5,4 L5.5,4.8 L4,5.5 Z" fill="var(--taupe)"/>
            <rect x="4" y="6.5" width="6" height="3.5" rx="0.6" fill="var(--taupe)"/>
          </svg>
          <span>11 4172-5036</span>
        </p>
      </div>

      <div class="address">
        <p>Al. Itapeva, 47, 3 andar</p>
        <p>Alphaville | Barueri/ SP</p>
        <p class="phone">
          <svg class="phone-icon" viewBox="0 0 14 12" aria-hidden="true">
            <rect x="0" y="0" width="14" height="12" rx="2" fill="var(--white)"/>
            <path d="M3,4 Q7,1 11,4 L10,5.5 L8.5,4.8 L8.5,4 Q7,3.4 5.5,4 L5.5,4.8 L4,5.5 Z" fill="var(--taupe)"/>
            <rect x="4" y="6.5" width="6" height="3.5" rx="0.6" fill="var(--taupe)"/>
          </svg>
          <span>11 6350-2481</span>
        </p>
      </div>
    </div>
  </section>

</main>
</body>
</html>
```